Business card for plumber

I need a business card for my plumbing company.
on it should:
Surname
position
E-mail
Telephone & mobile phone
Website
Please everything as placeholders / fantasy names.
We stand for high quality, hygiene and professionalism.

Colours:
# 606060 anthracite
# f7931e orange
# 2b89cc blue

Industry/Entity Type

Plumber

Contact Information for Business Card

folgt...

```html
<!DOCTYPE html>
<html lang="en">
<head>
<meta charset="utf-8">
<title>Vollmar Haustechnik – Business Card</title>
<link href="https://fonts.googleapis.com/css2?family=Open+Sans:wght@400;600;700&display=swap" rel="stylesheet">
<style>
  :root {
    --anthracite: #606060;
    --orange: #f7931e;
    --orange-deep: #ee9124;
    --blue: #2b89cc;
    --card: #f4f4f4;
    --page: #e4e4e4;
    --text-grey: #555555;
  }
  * { margin: 0; padding: 0; box-sizing: border-box; }
  html, body { width: 1200px; height: 960px; overflow: hidden; }
  body {
    background: var(--page);
    font-family: "Open Sans", Arial, sans-serif;
    position: relative;
  }
  .card {
    position: absolute;
    left: 342px;
    width: 519px;
    height: 336px;
    background: var(--card);
    overflow: hidden;
  }
  .card-front { top: 128px; }
  .card-back { top: 503px; }
  .card-shapes { position: absolute; inset: 0; }

  .service-list {
    position: absolute;
    left: 41px; top: 38px;
    list-style: none;
    color: #fff;
    font-weight: 700;
    font-size: 13px;
    line-height: 21.5px;
  }
  .service-list li::before { content: "• "; }

  .brand-name {
    position: absolute;
    color: var(--blue);
    font-weight: 700;
    text-transform: uppercase;
    line-height: 1;
  }
  .card-front .brand-name { left: 42px; top: 208px; font-size: 29px; }
  .card-front .brand-name span { display: block; font-size: 16px; letter-spacing: 4.2px; margin-top: 4px; }
  .card-front .site-url {
    position: absolute; left: 44px; top: 262px;
    font-size: 13px; color: var(--text-grey);
  }

  .brand-mark {
    position: absolute; left: 36px; top: 40px;
    width: 56px; height: 56px; border-radius: 50%;
    background: var(--orange);
  }
  .card-back .brand-name { left: 104px; top: 44px; font-size: 23px; }
  .card-back .brand-name span { display: block; font-size: 13px; letter-spacing: 3.4px; margin-top: 4px; }

  .holder { position: absolute; right: 32px; top: 176px; text-align: right; }
  .holder-name { color: var(--blue); font-weight: 700; font-size: 16px; line-height: 20px; }
  .holder-role { color: var(--text-grey); font-size: 13px; line-height: 18px; }

  .divider {
    position: absolute; left: 32px; right: 32px; top: 224px;
    height: 1.5px; background: #8a8a8a;
  }
  .contact-list {
    position: absolute; left: 32px; top: 237px;
    list-style: none; font-size: 13px; color: var(--text-grey);
    line-height: 18.5px;
  }
  .contact-list li { display: flex; align-items: center; gap: 6px; }
  .contact-list svg { width: 11px; height: 11px; fill: var(--orange); flex: none; }
  .card-back .site-url {
    position: absolute; right: 32px; top: 310px;
    font-size: 13px; color: #fff;
  }
</style>
</head>
<body>

<section class="card card-front">
  <svg class="card-shapes" viewBox="0 0 519 336" width="519" height="336">
    <path fill="var(--orange-deep)" d="M0 0 H408 L290 105 Q255 148 185 148 H0 Z"/>
    <path fill="var(--blue)" d="M0 319 H244 L230 336 H0 Z"/>
    <path fill="var(--anthracite)" d="M222 336 L252 308 Q258 304 270 304 H519 V336 Z"/>
    <circle cx="400" cy="190" r="55" fill="var(--blue)" opacity="0.12"/>
  </svg>
  <ul class="service-list">
    <li>PLUMBING</li>
    <li>HEATING 24H EMERGENCY SERVICE</li>
    <li>MAINTENANCE</li>
  </ul>
  <div class="brand-name">Vollmar<span>Haustechnik</span></div>
  <div class="site-url">www.vollmarhaustechnik.com</div>
</section>

<section class="card card-back">
  <svg class="card-shapes" viewBox="0 0 519 336" width="519" height="336">
    <path fill="var(--blue)" d="M0 319 H244 L230 336 H0 Z"/>
    <path fill="var(--orange-deep)" d="M224 336 L248 308 Q254 304 266 304 H519 V336 Z"/>
  </svg>
  <div class="brand-mark"></div>
  <div class="brand-name">Vollmar<span>Haustechnik</span></div>

  <div class="holder">
    <div class="holder-name">Daniel Hartmann</div>
    <div class="holder-role">President</div>
  </div>
  <div class="divider"></div>
  <ul class="contact-list">
    <li>
      <svg viewBox="0 0 12 12"><path d="M2.5 0.5 L4.5 3 L3.4 4.2 Q4.5 6.8 7.8 8.6 L9 7.5 L11.5 9.5 L10 11.5 Q4 11 0.5 2 Z"/></svg>
      555-014-2290
    </li>
    <li>
      <svg viewBox="0 0 12 12"><path d="M3 0 H9 V12 H3 Z M4 1.5 V9.5 H8 V1.5 Z" fill-rule="evenodd"/></svg>
      555-014-2290
    </li>
    <li>
      <svg viewBox="0 0 12 12"><path d="M0 2 H12 V10 H0 Z M1 3 L6 7 L11 3 Z" fill-rule="evenodd"/></svg>
      daniel@vollmarhaustechnik.com
    </li>
  </ul>
  <div class="site-url">www.vollmarhaustechnik.com</div>
</section>

</body>
</html>
```